New Web Design Project for kitchen company

We need a homepage mockup for a company that sells and installs kitchen and baths. Use your creative talent to come up with something visually appeal and professional for this web-site.

Please see the attached brief.

If you have any questions feel free to post them right on the project discussion.

Target Market(s)

homeowners

Number of Pages Required

1 page

Font styles to use
Serif
Other font styles liked:
• Something similar to the logo

```html
<!DOCTYPE html>
<html lang="en">
<head>
<meta charset="utf-8">
<title>Harborline Kitchen and Bath</title>
<link href="https://fonts.googleapis.com/css2?family=Marcellus&family=Montserrat:wght@400;500&family=Lato:wght@400;700&display=swap" rel="stylesheet">
<style>
:root{
  --ink:#111;
  --text:#333;
  --muted:#555;
  --band:#f2f2f2;
  --white:#fff;
  --footer:#000;
  --star:#f0a830;
  --line:#333;
}
*{box-sizing:border-box;margin:0;padding:0}
html,body{width:1200px;height:3297px;overflow:hidden;background:var(--white)}
body{position:relative;font-family:'Lato',sans-serif;color:var(--text)}
.abs{position:absolute}
.serif{font-family:'Marcellus',serif}
.brand{display:flex;align-items:center;gap:10px;font-family:'Marcellus',serif;font-size:22px;letter-spacing:1px}
.brand .dot{width:44px;height:44px;border-radius:50%;border:2px solid currentColor}
.btn{position:absolute;background:var(--ink);color:var(--white);border-radius:22px;font-family:'Montserrat',sans-serif;font-size:14px;display:flex;align-items:center;justify-content:center}
.nav a{position:absolute;top:48px;font-family:'Montserrat',sans-serif;font-size:13.5px;color:var(--text);text-decoration:none}
.nav a.active{color:var(--ink);font-weight:500}
.nav a.active:after{content:"";position:absolute;left:0;right:0;bottom:-12px;height:1px;background:var(--ink)}
.hero{left:0;top:107px;width:1200px;height:571px;
  background:
    radial-gradient(ellipse 260px 220px at 130px 420px,rgba(60,80,50,.55),transparent 70%),
    radial-gradient(ellipse 240px 260px at 1090px 360px,rgba(70,90,60,.5),transparent 70%),
    radial-gradient(ellipse 420px 200px at 760px 300px,rgba(200,205,212,.45),transparent 70%),
    linear-gradient(180deg,#8f9aa8 0%,#6f7b8a 40%,#4e5560 70%,#3a3a3c 100%)}
.hero-arrow{width:32px;height:32px;border-radius:50%;background:rgba(255,255,255,.35);color:var(--white);display:flex;align-items:center;justify-content:center;font-size:14px}
.dots{display:flex;gap:7px}
.dots span{width:6px;height:6px;border-radius:50%;background:#bbb}
.dots span.on{background:var(--white)}
.section-title{width:1200px;left:0;text-align:center;font-family:'Marcellus',serif;font-size:34px;color:var(--ink)}
.rule{width:36px;height:1px;background:var(--line)}
.about p{font-size:12px;line-height:15px;color:var(--text);margin-bottom:14px}
.services{left:0;top:1219px;width:1193px;height:541px;background:var(--band)}
.card{position:absolute;top:1338px;height:349px;background:var(--band);border:1px solid #e4e4e4;text-align:center}
.card.lift{background:var(--white);box-shadow:0 2px 8px rgba(0,0,0,.18)}
.card .ph{margin:4px 4px 0;height:198px}
.card h3{font-family:'Marcellus',serif;font-weight:400;font-size:18px;color:var(--ink);margin-top:18px}
.card .rule{margin:10px auto 12px}
.card p{font-size:13px;line-height:15px;color:var(--muted);padding:0 12px}
.circ{width:22px;height:22px;border:1px solid var(--ink);border-radius:50%;margin:14px auto 0;display:flex;align-items:center;justify-content:center;font-size:11px;color:var(--ink)}
.proj{position:absolute;width:333px;height:236px}
.testi{left:0;top:2504px;width:1200px;height:448px;background:var(--band)}
.tcard{left:225px;top:2623px;width:755px;height:227px;background:var(--white);text-align:center}
.arrow-sm{width:30px;height:30px;border-radius:50%;background:var(--white);display:flex;align-items:center;justify-content:center;font-size:13px;color:var(--ink)}
.footer{left:0;top:2952px;width:1200px;height:293px;background:var(--footer);color:var(--white)}
.footer h4{font-family:'Lato',sans-serif;font-weight:400;font-size:13px;letter-spacing:.3px}
.footer h4:after{content:"";display:block;width:38px;height:1px;background:var(--white);margin-top:10px}
.footer ul{list-style:none;font-family:'Montserrat',sans-serif;font-size:13px;line-height:22.5px}
.field{border:1px solid var(--white);border-radius:18px;height:36px;font-size:13px;display:flex;align-items:center}
.social{width:24px;height:24px;background:var(--ink);border-radius:50%}
</style>
</head>
<body>

<header>
  <div class="brand abs" style="left:74px;top:33px;color:var(--ink)"><span class="dot"></span>HARBORLINE</div>
  <nav class="nav">
    <a class="active" href="#" style="left:527px">Home</a>
    <a href="#" style="left:597px">About us</a>
    <a href="#" style="left:685px">Our Services</a>
    <a href="#" style="left:792px">Projects</a>
    <a href="#" style="left:877px">Contact us</a>
  </nav>
  <div class="btn" style="left:980px;top:36px;width:146px;height:37px">Get a Quote</div>
</header>

<section class="hero abs" role="img" aria-label="Photo of a bright open-plan kitchen with island, pendant lights and stainless appliances"></section>
<div class="hero-arrow abs" style="left:28px;top:358px">&lt;</div>
<div class="hero-arrow abs" style="left:1143px;top:358px">&gt;</div>
<div class="abs" style="left:0;top:340px;width:1200px;text-align:center;color:var(--white)">
  <div class="serif" style="font-size:20px">Welcome to</div>
  <div class="serif" style="font-size:34px;margin-top:2px">Harborline Kitchen and Bath</div>
  <div style="font-size:12.5px;line-height:15px;margin-top:6px">Lorem Ipsum simply dummy text of the printing and typesetting industry<br>has been the industry's standard dummy text ever since the 1500s,</div>
</div>
<div class="btn" style="left:522px;top:457px;width:155px;height:36px">Read More</div>
<div class="dots abs" style="left:578px;top:634px"><span class="on"></span><span></span><span></span><span></span></div>

<section class="about">
  <div class="section-title abs" style="top:728px">About us</div>
  <div class="rule abs" style="left:582px;top:775px"></div>
  <div class="abs" role="img" aria-label="Circular photo of a white kitchen island with pendant lights" style="left:153px;top:786px;width:390px;height:390px;border-radius:50%;border:8px solid #3a2c22;box-shadow:inset 0 0 0 6px #fff;background:radial-gradient(circle at 45% 35%,#f1efeb 0%,#d5d1c9 35%,#9a8e80 70%,#5e4b3c 100%)"></div>
  <h2 class="abs serif" style="left:601px;top:826px;width:480px;font-weight:400;font-size:29px;line-height:32px;color:var(--ink)">Our 30th Year in the Kitchen and Bath Industry!</h2>
  <div class="abs" style="left:603px;top:907px;width:460px">
    <p>Lorem Ipsum is simply dummy text of the printing and typesetting industry has been the industry's standard dummy text ever since the 1500s,</p>
    <p>when an unknown printer took a galley of type and scrambled it to make a type specimen book. It has survived not only five centuries, but also the leap into elect ronic typesetting, remaining essentially unchanged. It was popularised industries are in the 1960s</p>
    <p>with the release of Letraset sheets containing Lorem Ipsum passages, and more recently with desktop publishing software like Aldus PageMaker including ipsum text versions of Lorem Ipsum.</p>
  </div>
  <div class="btn" style="left:605px;top:1094px;width:147px;height:37px">Get a Quote</div>
</section>

<section class="services abs"></section>
<div class="section-title abs" style="top:1255px">Our Services</div>
<div class="rule abs" style="left:582px;top:1305px"></div>
<div class="card" style="left:70px;width:256px"><div class="ph" role="img" aria-label="Photo of a kitchen with marble counters" style="background:linear-gradient(180deg,#c9d2da 0%,#a7b2bd 45%,#d8d8d6 70%,#5b5c60 100%)"></div><h3>Kitchen Design</h3><div class="rule"></div><p>Lorem Ipsum is simply dummy text of and typesetting industry</p><div class="circ">&gt;</div></div>
<div class="card lift" style="left:343px;width:245px"><div class="ph" role="img" aria-label="Photo of a bathroom with freestanding tub" style="background:linear-gradient(180deg,#6f7a5c 0%,#c9c6b6 35%,#ece9e3 65%,#f7f6f3 100%)"></div><h3>Bath Design</h3><div class="rule"></div><p>Lorem Ipsum is simply dummy text of and typesetting industry</p><div class="circ">&gt;</div></div>
<div class="card" style="left:611px;width:246px"><div class="ph" role="img" aria-label="Photo of a white kitchen with dark counters and stools" style="background:linear-gradient(180deg,#e4e1da 0%,#c9c3b8 40%,#3c2e26 60%,#6a4e3a 100%)"></div><h3>Sales</h3><div class="rule"></div><p>Lorem Ipsum is simply dummy text of and typesetting industry</p><div class="circ">&gt;</div></div>
<div class="card" style="left:879px;width:247px"><div class="ph" role="img" aria-label="Photo of a tub being installed" style="background:linear-gradient(160deg,#c8cdd2 0%,#f0f1f2 40%,#e6e7e9 60%,#3a4a6a 85%,#4a4a4c 100%)"></div><h3>Installation Firm</h3><div class="rule"></div><p>Lorem Ipsum is simply dummy text of and typesetting industry</p><div class="circ">&gt;</div></div>

<div class="section-title abs" style="top:1805px">Our Projects</div>
<div class="proj" role="img" aria-label="Kitchen project with island and pendant lights" style="left:74px;top:1883px;background:linear-gradient(180deg,#e8e4da 0%,#cfc8ba 40%,#6e6864 65%,#3a3432 85%,#7a5a3a 100%)"></div>
<div class="proj" role="img" aria-label="Kitchen project with marble island and stools" style="left:434px;top:1883px;background:linear-gradient(180deg,#8d949c 0%,#c7ccd2 40%,#eceeef 65%,#5d6b82 100%)"></div>
<div class="proj" role="img" aria-label="Kitchen project with built-in shelves and wall ovens" style="left:792px;top:1883px;background:linear-gradient(90deg,#6e5a44 0%,#b39f82 30%,#e0d8ca 60%,#c9bfae 100%)"></div>
<div class="proj" role="img" aria-label="Kitchen sink under a window" style="left:74px;top:2144px;background:linear-gradient(180deg,#d8dadc 0%,#b9bcc0 45%,#8a8c90 60%,#a9a9ab 100%)"></div>
<div class="proj" role="img" aria-label="Kitchen project shown dimmed behind caption" style="left:434px;top:2144px;background:linear-gradient(180deg,#2f3236,#202225)"></div>
<div class="abs" style="left:451px;top:2270px;color:var(--white)">
  <div class="serif" style="font-size:18px">Project Title</div>
  <div style="font-size:12.5px;line-height:15px;margin-top:10px">Lorem Ipsum is simply dummy text typesetting<br>in the industry.</div>
  <svg width="14" height="14" style="margin-top:6px" viewBox="0 0 14 14"><circle cx="7" cy="7" r="6" fill="none" stroke="#fff"/><path d="M4 7h6M7.5 4.5 10 7 7.5 9.5" fill="none" stroke="#fff"/></svg>
</div>
<div class="proj" role="img" aria-label="Kitchen range with subway tile backsplash" style="left:792px;top:2144px;background:linear-gradient(180deg,#f0f0ee 0%,#dcdcda 40%,#5c5a58 60%,#e8e8e6 75%,#9a8a78 100%)"></div>
<div class="btn" style="left:526px;top:2410px;width:147px;height:36px">View More</div>

<section class="testi abs"></section>
<div class="section-title abs" style="top:2543px">Testimonials</div>
<div class="abs" style="left:0;top:2589px;width:1200px;text-align:center;font-size:12.5px">What Clients say about us</div>
<div class="tcard abs">
  <div class="serif" style="font-size:30px;margin-top:8px;line-height:26px;color:var(--ink)">&ldquo;</div>
  <p style="font-size:12px;line-height:15.5px;padding:6px 44px 0;color:var(--text)">Harborline Kitchens Inc. had done an awesome remodeling of my wife's kitchen several years ago so I called on them to remodel my bathroom as it was in need of a lot of work. Mark and his crew of professionals came in and did an amazing job. Mark and his wife helped pick out just the right vanity, knobs, countertop and flooring to match. They coordinated the carpenter, plumber, electrician and plaster. He kept in contact throughout the whole remodeling process. If you're looking to get an excellent remodeling at a reasonable price call Harborline Kitchens you will not be disappointed.</p>
  <div style="font-family:'Montserrat',sans-serif;font-size:15px;margin-top:14px;color:var(--ink)">Laura Whitcombe</div>
  <div style="color:var(--star);font-size:12px;letter-spacing:3px;margin-top:10px">★★★★★</div>
</div>
<div class="arrow-sm abs" style="left:176px;top:2714px">&lt;</div>
<div class="arrow-sm abs" style="left:1008px;top:2714px">&gt;</div>
<div class="dots abs" style="left:583px;top:2881px"><span style="background:var(--ink)"></span><span></span><span></span></div>

<footer class="footer abs">
  <div class="brand abs" style="left:74px;top:72px;color:var(--white)"><span class="dot"></span>HARBORLINE</div>
  <p class="abs" style="left:74px;top:140px;width:240px;font-size:12px;line-height:15px">Lorem Ipsum is simply dummy text of the printing and typesetting industry has been the industry's standard.</p>
  <div class="abs" style="left:74px;top:205px;font-size:12px;text-decoration:underline">Read More</div>

  <div class="abs" style="left:415px;top:62px">
    <h4>QUICK LINKS</h4>
    <ul style="margin-top:18px"><li>&gt;&nbsp;&nbsp;&nbsp;&nbsp;Home</li><li>&gt;&nbsp;&nbsp;&nbsp;&nbsp;About us</li><li>&gt;&nbsp;&nbsp;&nbsp;&nbsp;Our Services</li><li>&gt;&nbsp;&nbsp;&nbsp;&nbsp;Projects</li><li>&gt;&nbsp;&nbsp;&nbsp;&nbsp;Contact us</li></ul>
  </div>

  <div class="abs" style="left:606px;top:62px">
    <h4>CONTACT INFO</h4>
    <div style="margin-top:18px;font-size:13px;line-height:22.5px">
      <div><svg width="12" height="12" viewBox="0 0 12 12"><path d="M2 1h2.5l1 3-1.5 1a7 7 0 0 0 3 3l1-1.5 3 1V10a1 1 0 0 1-1 1C5 11 1 7 1 2a1 1 0 0 1 1-1z" fill="#fff"/></svg>&nbsp;&nbsp;&nbsp;555-014-7100</div>
      <div><svg width="12" height="10" viewBox="0 0 12 10"><rect x="0.5" y="0.5" width="11" height="9" fill="#fff"/><path d="M.5.5 6 5l5.5-4.5" fill="none" stroke="#000"/></svg>&nbsp;&nbsp;&nbsp;hello@harborlinekb.com</div>
      <div><svg width="12" height="13" viewBox="0 0 12 13"><path d="M6 12S1.5 7 1.5 4.5a4.5 4.5 0 0 1 9 0C10.5 7 6 12 6 12z" fill="#fff"/><circle cx="6" cy="4.5" r="1.6" fill="#000"/></svg>&nbsp;&nbsp;&nbsp;48 Maple Ave.</div>
      <div style="padding-left:24px">Brookfield, NY 12345</div>
    </div>
  </div>

  <div class="abs" style="left:861px;top:62px;width:265px">
    <h4>NEWSLETTER</h4>
    <div class="field" style="margin-top:42px;padding-left:14px">Your Email</div>
    <div class="field" style="margin-top:8px;background:var(--white);color:var(--ink);justify-content:center">Subscrieb Now</div>
  </div>
</footer>

<div class="abs" style="left:74px;top:3266px;font-size:12px;color:var(--text)">Copyright © 2020 HARBORLINE . All Right Reserved</div>
<div class="abs" style="left:1006px;top:3258px;display:flex;gap:8px" aria-label="Social links">
  <span class="social"></span><span class="social"></span><span class="social"></span><span class="social"></span>
</div>

</body>
</html>
```